TBrandow executive consulting

We need a basic clean website for executive consulting. Rosalind is the previos CIO for bluecrest skyways and currently supports several technology companies with innovation and transformation.

Target Market(s)

C level technology and CIO training

Industry/Entity Type

Technology and travel industry

Coding

Coded - Design and coding required

Number of Pages Required

3 page

Font styles to use
Sans Serif

Colors
0054AA
0677BA
7BADD7
CADEEF
E8F1F8
0094D4
00A9DD
6FCCEA
C7EBF8
E9F6FB

Requirements
Must have
• Home page, about us, services social media links

```html
<!DOCTYPE html>
<html lang="en">
<head>
<meta charset="UTF-8">
<title>TBrandow Executive Consulting</title>
<link rel="stylesheet" href="https://fonts.googleapis.com/css2?family=Poppins:wght@500;600;700&family=Outfit:wght@300;400;500;600&display=swap">
<style>
:root{
  --navy:#0d1458;
  --indigo:#1b1a9a;
  --violet:#3a22b8;
  --blue:#0054aa;
  --cyan:#00a9dd;
  --sky:#0094d4;
  --light:#c7ebf8;
  --pale:#e9f6fb;
  --white:#ffffff;
  --panel:#0f1a5c;
  --footer:#081038;
  --star:#ffd21e;
}
*{box-sizing:border-box;margin:0;padding:0}
html,body{width:1200px;height:5376px;overflow:hidden}
body{
  position:relative;
  font-family:"Outfit",sans-serif;
  color:var(--white);
  background:
    radial-gradient(ellipse 700px 300px at 600px 1700px,rgba(0,169,221,.55),transparent 70%),
    radial-gradient(ellipse 500px 400px at 1000px 1300px,rgba(0,148,212,.45),transparent 70%),
    radial-gradient(ellipse 600px 400px at 150px 1950px,rgba(150,60,220,.45),transparent 70%),
    radial-gradient(ellipse 700px 300px at 600px 4100px,rgba(0,169,221,.5),transparent 70%),
    radial-gradient(ellipse 500px 400px at 300px 3300px,rgba(60,40,200,.5),transparent 70%),
    linear-gradient(180deg,#1c1f8e 0%,#2a1fae 8%,#1a2aa0 20%,#161c86 35%,#1f1aa6 50%,#1a24a0 62%,#1b2c9c 72%,#101a70 85%,#081038 88%,#081038 100%);
}
.abs{position:absolute}
.orb{position:absolute;border-radius:50%;background:radial-gradient(circle at 35% 35%,#6fcaff,#1a5ce0 55%,#0b2a8a)}
.photo{position:absolute;overflow:hidden}
.btn{position:absolute;display:flex;align-items:center;justify-content:center;gap:8px;background:var(--sky);border:2px solid var(--light);border-radius:30px;color:#fff;font-weight:600;font-size:17px}
.btn svg{width:12px;height:12px}

/* nav */
.logo{font-family:"Poppins",sans-serif;font-weight:600;font-size:40px;color:#fff;display:flex;align-items:center;gap:10px}
.logo i{display:block;width:14px;height:14px;border-radius:50%;border:2px solid #fff}
.nav a{position:absolute;top:38px;font-size:16px;font-weight:500;color:#fff;text-decoration:none}
.nav .active::after{content:"";position:absolute;left:0;right:0;bottom:-12px;height:3px;background:var(--cyan)}

/* hero */
.hero-title{left:106px;top:196px;font-family:"Poppins",sans-serif;font-weight:700;font-size:62px;line-height:74px}
.hero-text{left:108px;top:362px;width:345px;font-size:21px;line-height:31px}
.follow{left:108px;top:614px;display:flex;align-items:center;gap:14px;font-size:15px;font-weight:500}
.follow .rule{width:48px;height:1px;background:#fff}
.socials{display:flex;gap:8px}
.socials span{width:32px;height:32px;border-radius:50%;border:1.5px solid #fff;display:block}

/* about */
.eyebrow{font-size:24px;letter-spacing:4px;font-weight:400}
.about-title{left:102px;top:846px;font-family:"Poppins",sans-serif;font-weight:600;font-size:58px;line-height:67px;letter-spacing:1.5px}
.about-rule{left:108px;top:1091px;width:978px;height:2px;background:rgba(199,235,248,.7)}
.about-text{left:355px;top:1146px;width:470px;font-size:17.5px;line-height:27.5px;color:#d9e4f6}

/* stats */
.section-title{left:0;width:1200px;text-align:center;font-family:"Poppins",sans-serif;font-weight:600;font-size:56px}
.stats{left:108px;top:1661px;width:981px;height:188px;background:rgba(13,20,88,.85);border-radius:6px;display:flex;align-items:center}
.stat{flex:1;text-align:center;position:relative}
.stat + .stat::before{content:"";position:absolute;left:0;top:-6px;height:100px;width:1px;background:rgba(199,235,248,.35)}
.stat b{display:block;font-family:"Poppins",sans-serif;font-size:56px;font-weight:600;line-height:64px}
.stat span{display:block;font-size:21px;line-height:26px;width:200px;margin:6px auto 0}

/* meet */
.meet-name{left:606px;top:2078px;font-family:"Poppins",sans-serif;font-weight:600;font-size:52px;white-space:nowrap}
.meet-text{left:611px;top:2176px;width:470px;font-size:17.5px;line-height:27.5px;color:#e1e8f8}

/* services */
.card{position:absolute;width:224px;height:223px;border:2px solid rgba(199,235,248,.55);border-radius:4px;overflow:visible}
.card .bg{position:absolute;inset:0;background:linear-gradient(160deg,#2f3a9a,#1a2576 60%,#121a5e)}
.card .icon{position:absolute;left:61px;top:-30px;width:102px;height:102px;border-radius:50%;background:var(--sky);border:4px solid #fff;display:flex;align-items:center;justify-content:center}
.card .icon svg{width:54px;height:54px;fill:none;stroke:#fff;stroke-width:2.4;stroke-linecap:round;stroke-linejoin:round}
.card h3{position:absolute;left:0;right:0;top:96px;text-align:center;font-family:"Poppins",sans-serif;font-weight:500;font-size:22px;line-height:29px}
.card.cta{background:var(--sky);border-color:var(--sky)}
.card.cta h3{top:36px;font-weight:600}
.card.cta p{position:absolute;top:100px;left:0;right:0;text-align:center;font-size:15px;line-height:20px;font-weight:600}
.card.cta a{position:absolute;top:160px;left:0;right:0;text-align:center;color:#fff;font-weight:600;font-size:19px;text-decoration:underline}

/* testimonial */
.testi{left:167px;top:3615px;width:868px;height:419px;background:#0a1450;border-radius:6px}
.testi-inner{left:184px;top:3642px;width:832px;height:319px;background:#142070;border-radius:4px;padding:38px 50px 0;text-align:center;font-size:16.5px;line-height:23px;color:#d7e0f4}
.testi-inner .who{margin-top:18px;font-size:19px;color:#fff}
.testi-inner .who b{font-weight:600}
.quote{position:absolute;width:52px;height:52px;border-radius:50%;background:var(--sky);display:flex;align-items:center;justify-content:center;font-family:"Poppins",sans-serif;font-weight:700;font-size:44px;line-height:1;padding-top:20px}
.stars{left:0;width:1200px;top:3984px;text-align:center;color:var(--star);font-size:26px;letter-spacing:2px}

/* contact */
.contact{left:104px;top:4180px;width:987px;height:426px;background:#0e1a5e;border-radius:4px}
.contact-title{left:543px;top:4206px;font-family:"Poppins",sans-serif;font-weight:600;font-size:56px}
.field{position:absolute;background:#fff;border-radius:3px;color:#3a4a7a;font-size:16px;display:flex;align-items:center;gap:8px;padding-left:12px}
.field svg{width:13px;height:13px;fill:var(--blue)}
.field.msg{align-items:flex-start;padding-top:10px}

/* footer */
.footer-band{left:0;top:4737px;width:1200px;height:639px;background:var(--footer)}
.footer{left:38px;top:4825px;width:1114px;height:482px;background:linear-gradient(180deg,#0d1a5e,#0b1550);border:1px solid rgba(199,235,248,.2);border-radius:6px}
.f-head{font-size:20px;font-weight:600;position:absolute}
.f-head::after{content:"";position:absolute;left:0;bottom:-8px;width:36px;height:2px;background:var(--cyan)}
.f-list{position:absolute;list-style:none;font-size:16px;line-height:21px;color:#d7e0f4}
.f-list li{position:relative;padding-left:16px;margin-bottom:10px}
.f-list li::before{content:"›";position:absolute;left:0;top:-1px;color:var(--cyan)}
.c-row{position:absolute;left:860px;display:flex;align-items:center;gap:22px;font-size:16px;line-height:21px;color:#e1e8f8}
.c-ic{width:36px;height:36px;border-radius:50%;background:var(--sky);display:flex;align-items:center;justify-content:center;flex:none}
.c-ic svg{width:18px;height:18px;fill:#fff}
.copy{left:0;width:1200px;top:5230px;text-align:center;font-size:16px;color:#e1e8f8}
.copy em{font-style:normal;color:var(--cyan)}
</style>
</head>
<body>

<div class="orb" style="left:2px;top:156px;width:78px;height:78px" aria-hidden="true"></div>
<div class="orb" style="left:1106px;top:872px;width:80px;height:80px" aria-hidden="true"></div>
<div class="orb" style="left:1114px;top:2220px;width:80px;height:80px" aria-hidden="true"></div>
<div class="orb" style="left:138px;top:3544px;width:82px;height:82px" aria-hidden="true"></div>
<div class="orb" style="left:1058px;top:4148px;width:78px;height:78px" aria-hidden="true"></div>

<header>
  <div class="abs logo" style="left:108px;top:22px">TB<i></i></div>
  <nav class="nav">
    <a class="active" style="left:459px">HOME</a>
    <a style="left:558px">ABOUT</a>
    <a style="left:663px">SERVICES</a>
  </nav>
</header>

<div class="photo" role="img" aria-label="Smiling colleagues working together at a desk with a globe" style="left:500px;top:-20px;width:712px;height:700px;border-radius:50%;background:radial-gradient(circle at 45% 40%,#e9d8c8,#b98e6e 45%,#6d5446 75%,#3b3260)"></div>
<div class="btn" style="left:943px;top:29px;width:148px;height:42px;font-size:14px">
  <svg viewBox="0 0 24 24" style="width:15px;height:15px;fill:#fff"><path d="M6.6 10.8a15 15 0 006.6 6.6l2.2-2.2c.3-.3.7-.4 1-.2 1.1.4 2.3.6 3.6.6.6 0 1 .4 1 1V20c0 .6-.4 1-1 1A17 17 0 013 4c0-.6.4-1 1-1h3.5c.6 0 1 .4 1 1 0 1.3.2 2.5.6 3.6.1.3 0 .7-.2 1z"/></svg>
  555-010-2040
</div>
<h1 class="abs hero-title">Innovation &amp;<br>Transformation</h1>
<p class="abs hero-text">We don't just help organizations adapt to change— we help them lead it.</p>
<div class="btn" style="left:108px;top:480px;width:197px;height:46px">Get Started Now
  <svg viewBox="0 0 12 12"><path d="M2 10L10 2M4 2h6v6" stroke="#fff" stroke-width="1.6" fill="none"/></svg></div>
<div class="abs follow">FOLLOW US <span class="rule"></span>
  <div class="socials" aria-label="Social media links"><span></span><span></span><span></span><span></span></div>
</div>

<p class="abs eyebrow" style="left:108px;top:806px">ABOUT US</p>
<h2 class="abs about-title">Support Technology<br>Companies With Innovation<br>And Transformation</h2>
<div class="abs about-rule"></div>
<div class="photo" role="img" aria-label="Executive working at a laptop in an office" style="left:109px;top:1127px;width:208px;height:208px;border-radius:50%;background:linear-gradient(135deg,#e9eef3,#9aa6b6 55%,#3b4454)"></div>
<p class="abs about-text">Rosalind Brandow is a seasoned leader with a remarkable 40-year career in the travel industry, including 20 transformative years at Bluecrest Skyways. As the Senior Vice President of Technology (CIO), Rosalind spearheaded some of the company's most significant technological and strategic transformations,</p>
<div class="btn" style="left:355px;top:1375px;width:146px;height:45px">Read More
  <svg viewBox="0 0 12 12"><path d="M2 10L10 2M4 2h6v6" stroke="#fff" stroke-width="1.6" fill="none"/></svg></div>
<div class="photo" role="img" aria-label="Business team reviewing documents together" style="left:860px;top:1144px;width:342px;height:342px;border-radius:50%;background:radial-gradient(circle at 50% 40%,#d7dbe2,#8a93a5 50%,#394257)"></div>

<h2 class="abs section-title" style="top:1564px">Our Statistics</h2>
<div class="abs stats">
  <div class="stat"><b>20+</b><span>20 transformative years</span></div>
  <div class="stat"><b>20+</b><span>Technology Teams</span></div>
  <div class="stat"><b>40+</b><span>Career in the travel industry,</span></div>
</div>

<div class="photo" role="img" aria-label="Portrait of Rosalind Brandow in front of a passenger aircraft" style="left:104px;top:2003px;width:480px;height:480px;border-radius:50%;border:12px solid #f2f4f8;background:linear-gradient(180deg,#9fb3c8 0%,#c7d2dc 40%,#3a4fa0 55%,#2b2b3a 100%)"></div>
<p class="abs eyebrow" style="left:611px;top:2036px">MEET</p>
<h2 class="abs meet-name">Rosalind Brandow</h2>
<p class="abs meet-text">Rosalind A. Brandow is a retired Chief Executive Officer and Executive Advisor of Bluecrest Skyways Airlines, a role she held from 2017 until December 2024. In this capacity, Ms. Brandow oversaw key strategic initiatives, including advising senior leadership on the company's technology roadmap Officer.</p>
<div class="btn" style="left:611px;top:2404px;width:149px;height:46px">Read More
  <svg viewBox="0 0 12 12"><path d="M2 10L10 2M4 2h6v6" stroke="#fff" stroke-width="1.6" fill="none"/></svg></div>

<h2 class="abs section-title" style="top:2648px">Our Services</h2>

<div class="card" style="left:104px;top:2807px">
  <div class="bg" role="img" aria-label="Executives in a meeting"></div>
  <div class="icon"><svg viewBox="0 0 48 48"><circle cx="24" cy="16" r="6"/><circle cx="11" cy="20" r="4"/><circle cx="37" cy="20" r="4"/><path d="M13 38c0-7 5-12 11-12s11 5 11 12M4 36c0-5 3-8 7-8M44 36c0-5-3-8-7-8"/></svg></div>
  <h3>Leadership<br>Mentorship</h3>
</div>
<div class="card" style="left:359px;top:2807px">
  <div class="bg" role="img" aria-label="Professionals discussing strategy"></div>
  <div class="icon"><svg viewBox="0 0 48 48"><circle cx="24" cy="24" r="7"/><path d="M24 6v6M24 36v6M6 24h6M36 24h6M11 11l4 4M33 33l4 4M37 11l-4 4M15 33l-4 4"/></svg></div>
  <h3>Technology<br>Strategy<br>Development</h3>
</div>
<div class="card" style="left:616px;top:2807px">
  <div class="bg" role="img" aria-label="Team working with digital devices"></div>
  <div class="icon"><svg viewBox="0 0 48 48"><rect x="14" y="6" width="20" height="36" rx="3"/><path d="M20 14h8M19 22h10M19 28h10M22 37h4"/></svg></div>
  <h3>Digital<br>Transformation<br>Consulting</h3>
</div>
<div class="card" style="left:868px;top:2807px">
  <div class="bg" role="img" aria-label="Business partners shaking hands"></div>
  <div class="icon"><svg viewBox="0 0 48 48"><path d="M4 22l8-8 8 4 6-4 10 2 8 6M12 14l-8 12 14 12 6-2M36 16l8 10-14 12-8-6M20 30l4 4M24 26l6 6"/></svg></div>
  <h3>IT-Business<br>Partnership<br>Development</h3>
</div>

<div class="card" style="left:104px;top:3097px">
  <div class="bg" role="img" aria-label="Executive presenting to a team"></div>
  <div class="icon"><svg viewBox="0 0 48 48"><rect x="12" y="12" width="24" height="26" rx="3"/><path d="M18 20h12M18 26h12M18 32h8M24 6v6M6 25h6M36 25h6"/></svg></div>
  <h3>Organizational<br>Change<br>Management</h3>
</div>
<div class="card" style="left:359px;top:3097px">
  <div class="bg" role="img" aria-label="Project team reviewing plans"></div>
  <div class="icon"><svg viewBox="0 0 48 48"><rect x="6" y="8" width="32" height="24" rx="2"/><path d="M14 17l-3 3 3 3M22 17l3 3-3 3M12 38h18"/><circle cx="36" cy="34" r="6"/></svg></div>
  <h3>Program and<br>Project<br>Oversight</h3>
</div>
<div class="card" style="left:616px;top:3097px">
  <div class="bg" role="img" aria-label="Advisor meeting with executives"></div>
  <div class="icon"><svg viewBox="0 0 48 48"><rect x="8" y="8" width="26" height="20" rx="3"/><path d="M14 28v8l6-8M16 16h10M16 21h6M34 18h6v16h-6v6l-6-6h-8"/></svg></div>
  <h3>Advisory<br>Services for<br>CIOs and IT<br>Executives</h3>
</div>
<div class="card cta" style="left:868px;top:3097px">
  <h3>We're here<br>ForYou</h3>
  <p>Let explore how TB<br>Work for you</p>
  <a>Contact us</a>
</div>

<h2 class="abs section-title" style="top:3512px;left:-14px">Testimonial</h2>
<div class="abs testi"></div>
<div class="abs testi-inner">
  <p>Rosalind is a decisive and fair leader who exemplifies strength, wisdom, and empathy. She always possesses a clear vision for the future and is willing to make bold decisions which are grounded in data, expertise, and intuition while remaining open to diverse perspectives.<br>Rosalind's leadership style fosters an inclusive environment where every voice matters, empowering her team to excel and innovate. She was able to balance ambition with humanity and succeeded in prioritizing the well-being of her people, ensuring they feel valued and supported.<br>In times of uncertainty her unwavering confidence and fairness inspire trust, driving the organization forward with resilience and integrity.</p>
  <p class="who"><b>Daniel Forsythe,</b> CEO Norvale</p>
</div>
<div class="quote" style="left:147px;top:3701px">“</div>
<div class="quote" style="left:999px;top:3701px">”</div>
<div class="abs stars">★★★★★</div>

<div class="abs contact"></div>
<div class="photo" role="img" aria-label="Two colleagues reviewing work at a laptop" style="left:104px;top:4118px;width:410px;height:488px;border-radius:0 0 0 4px;clip-path:path('M0 68 L200 68 C330 40 420 180 410 300 L410 488 L0 488 Z');background:linear-gradient(160deg,#f1f1f3,#b8bcc6 45%,#3a3f58)"></div>
<h2 class="abs contact-title">Contact Us</h2>
<div class="field" style="left:543px;top:4285px;width:254px;height:46px"><svg viewBox="0 0 12 12"><circle cx="6" cy="3.5" r="2.5"/><path d="M1 12c0-3 2-5 5-5s5 2 5 5z"/></svg>First Name</div>
<div class="field" style="left:806px;top:4285px;width:252px;height:46px"><svg viewBox="0 0 12 12"><circle cx="6" cy="3.5" r="2.5"/><path d="M1 12c0-3 2-5 5-5s5 2 5 5z"/></svg>Last Name</div>
<div class="field" style="left:543px;top:4339px;width:254px;height:46px"><svg viewBox="0 0 12 12"><rect x="0" y="2" width="12" height="8" rx="1"/></svg>Email</div>
<div class="field" style="left:806px;top:4339px;width:252px;height:46px"><svg viewBox="0 0 24 24"><path d="M6.6 10.8a15 15 0 006.6 6.6l2.2-2.2c.3-.3.7-.4 1-.2 1.1.4 2.3.6 3.6.6.6 0 1 .4 1 1V20c0 .6-.4 1-1 1A17 17 0 013 4c0-.6.4-1 1-1h3.5c.6 0 1 .4 1 1 0 1.3.2 2.5.6 3.6.1.3 0 .7-.2 1z"/></svg>Phone</div>
<div class="field msg" style="left:543px;top:4395px;width:515px;height:117px"><svg viewBox="0 0 12 12"><rect x="0" y="2" width="12" height="8" rx="1"/></svg>Message</div>
<div class="btn" style="left:543px;top:4525px;width:150px;height:46px">Submit Now
  <svg viewBox="0 0 12 12"><path d="M2 10L10 2M4 2h6v6" stroke="#fff" stroke-width="1.6" fill="none"/></svg></div>

<div class="abs footer-band"></div>
<footer class="abs footer"></footer>
<div class="abs logo" style="left:92px;top:4866px">TB<i></i></div>
<p class="abs" style="left:108px;top:4946px;width:245px;font-size:16px;line-height:25px;color:#d7e0f4">Rosalind Brandow is a seasoned leader with a remarkable 40-year career in the travel industry,including 20 transformative years at Bluecrest Skyways.</p>
<div class="abs socials" style="left:108px;top:5140px" aria-label="Social media links"><span></span><span></span><span></span><span></span></div>

<h4 class="f-head" style="left:380px;top:4864px">Services</h4>
<ul class="f-list" style="left:380px;top:4920px;width:220px">
  <li>Leadership Mentorship</li>
  <li>Technology Strategy Development</li>
  <li>Digital Transformation Consulting</li>
  <li>IT-Business Partnership Development</li>
</ul>
<ul class="f-list" style="left:608px;top:4920px;width:220px">
  <li>Organizational Change Management</li>
  <li>Program and Project Oversight</li>
  <li>Advisory Services for CIOs and IT Executives</li>
</ul>

<h4 class="f-head" style="left:860px;top:4864px">Contact</h4>
<div class="c-row" style="top:4922px"><span class="c-ic"><svg viewBox="0 0 24 24"><path d="M12 2a7 7 0 00-7 7c0 5 7 13 7 13s7-8 7-13a7 7 0 00-7-7zm0 9.5A2.5 2.5 0 1112 6.5a2.5 2.5 0 010 5z"/></svg></span>2210 Harbor Lane,<br>Austin, Texas, 78701</div>
<div class="c-row" style="top:4990px"><span class="c-ic"><svg viewBox="0 0 24 24"><path d="M6.6 10.8a15 15 0 006.6 6.6l2.2-2.2c.3-.3.7-.4 1-.2 1.1.4 2.3.6 3.6.6.6 0 1 .4 1 1V20c0 .6-.4 1-1 1A17 17 0 013 4c0-.6.4-1 1-1h3.5c.6 0 1 .4 1 1 0 1.3.2 2.5.6 3.6.1.3 0 .7-.2 1z"/></svg></span>1-800-555-0199</div>
<div class="c-row" style="top:5048px"><span class="c-ic"><svg viewBox="0 0 24 24"><path d="M3 5h18v14H3z M3 5l9 7 9-7" stroke="#0094d4" stroke-width="1.5"/></svg></span>tb@brandowconsult.com</div>

<p class="abs copy">Copyright 2025<em>TB</em>. All Rights Reserved</p>

</body>
</html>
```